Business card design for online Mandarin Learning School

We need a business card design for our online language learning school called "Maple Bridge Online for Mandarin Learning". Our existing website is https://www.maplebridgeonline.com
We have our logo already. We would like to see our business card design that can make our online teaching services to be innovative, young, energetic and fun to learn. Prefer to have a certain level of color matching with our website. Apart from "Maple Bridge Online", need to specifically state "for Mandarin Learning" as well on the business card.

```html
<!DOCTYPE html>
<html lang="en">
<head>
<meta charset="utf-8">
<title>Maple Bridge Online for Mandarin Learning – Business Card</title>
<link rel="stylesheet" href="https://fonts.googleapis.com/css2?family=Roboto:wght@400;500&display=swap">
<style>
  :root {
    --stage: #2b2b2c;
    --card: #1f2021;
    --teal: #1fb0bd;
    --coral: #e8625f;
    --text: #ecedee;
    --muted: #cfd1d3;
    --rule: #d9dadb;
    --pattern-a: #232425;
    --pattern-b: #1c1d1e;
  }
  * { box-sizing: border-box; margin: 0; padding: 0; }
  html, body {
    width: 1200px; height: 1200px; overflow: hidden;
    background: var(--stage);
    font-family: "Roboto", Arial, sans-serif;
  }
  .stage { position: relative; width: 1200px; height: 1200px; }
  .card {
    position: absolute; left: 120px; width: 960px; height: 548px;
    background: var(--card);
    overflow: hidden;
  }
  .card--back { top: 36px; }
  .card--front { top: 616px; }

  .back-pattern {
    position: absolute; inset: 0;
    background: radial-gradient(circle at 40% 40%, var(--pattern-a), var(--pattern-b));
  }

  .brand {
    position: absolute;
    display: flex; align-items: center;
    color: var(--teal); font-weight: 500;
  }
  .brand__name { display: block; text-align: right; }
  .brand__line { display: block; white-space: nowrap; }
  .brand-dot { flex: none; border-radius: 50%; background: var(--coral); }

  .brand--back { right: 70px; bottom: 90px; gap: 12px; font-size: 20px; line-height: 26px; }
  .brand--back .brand-dot { width: 14px; height: 14px; }

  .brand--front { right: 70px; top: 112px; gap: 16px; font-size: 34px; line-height: 44px; letter-spacing: 0.5px; }
  .brand--front .brand-dot { width: 22px; height: 22px; }

  .person { position: absolute; left: 126px; top: 214px; }
  .person__name {
    color: var(--teal); font-weight: 500; font-size: 46px; letter-spacing: 1px;
    text-transform: uppercase; line-height: 1;
  }
  .person__role { color: var(--muted); font-size: 24px; margin-top: 2px; }
  .divider {
    position: absolute; left: 126px; right: 70px; top: 318px;
    height: 1px; background: var(--rule);
  }
  .contacts { position: absolute; left: 126px; top: 336px; list-style: none; }
  .contacts li {
    display: flex; align-items: center; gap: 12px;
    color: var(--text); font-size: 26px; letter-spacing: 1px;
    line-height: 38px;
  }
  .contacts svg { width: 20px; height: 20px; flex: none; }
</style>
</head>
<body>
<main class="stage">
  <section class="card card--back" aria-label="Card back">
    <div class="back-pattern" role="img" aria-label="Faint tone-on-tone repeating brand pattern"></div>
    <div class="brand brand--back">
      <span class="brand-dot"></span>
      <span class="brand__name">
        <span class="brand__line">Maple Bridge Online</span>
        <span class="brand__line">for Mandarin Learning</span>
      </span>
    </div>
  </section>

  <section class="card card--front" aria-label="Card front">
    <div class="brand brand--front">
      <span class="brand-dot"></span>
      <span class="brand__name">
        <span class="brand__line">Maple Bridge Online</span>
        <span class="brand__line">for Mandarin Learning</span>
      </span>
    </div>

    <div class="person">
      <h1 class="person__name">Nora Vell</h1>
      <p class="person__role">Manager</p>
    </div>

    <div class="divider"></div>

    <ul class="contacts">
      <li>
        <svg viewBox="0 0 20 20" aria-hidden="true"><rect x="5" y="1.5" width="10" height="17" rx="2" fill="none" stroke="#e8625f" stroke-width="2"/><circle cx="10" cy="15" r="1.2" fill="#e8625f"/></svg>
        000-000-0000
      </li>
      <li>
        <svg viewBox="0 0 20 20" aria-hidden="true"><path d="M4 2l4 1 1 4-2 2c1 2.5 3 4.5 5.5 5.5l2-2 4 1 1 4c-1 1.2-2.5 1.5-4 1C9 17 3 11 2 6 1.5 4.5 2.5 3 4 2z" fill="#e8625f"/></svg>
        000-000-0000
      </li>
      <li>
        <svg viewBox="0 0 20 20" aria-hidden="true"><rect x="1.5" y="4" width="17" height="12" fill="#e8625f"/><path d="M1.5 4l8.5 7 8.5-7" fill="none" stroke="#1f2021" stroke-width="1.5"/></svg>
        info@maplebridgeonline.com
      </li>
      <li>
        <svg viewBox="0 0 20 20" aria-hidden="true"><circle cx="10" cy="10" r="8" fill="none" stroke="#e8625f" stroke-width="1.6"/><ellipse cx="10" cy="10" rx="3.5" ry="8" fill="none" stroke="#e8625f" stroke-width="1.2"/><path d="M2 10h16M3.5 6h13M3.5 14h13" stroke="#e8625f" stroke-width="1.2"/></svg>
        www.maplebridgeonline.com
      </li>
    </ul>
  </section>
</main>
</body>
</html>
```